Business Recognition Design

We need a design for a recognition to be given to business leaders in our community.
The recognition shall be made on a brass plaque on wood panel background (picture attached, please use it as a background), and all drawing must be in vectors and only one color (black).
It should also have a logo on the top and signature on the right bottom.
The text is enclosed in DOC file.
Updates

Reason: just to be able to find the best solution

Reason: None of the suggestion is good enough. Logo in general is too big in comparison with the rest of the plate.

Industry/Entity Type

Business

Requirements
Must have
• - standard Windows font (or possibility to install the same font on Windows), as the name on the recognition shall be printed in the same font
Nice to have
• - some graphic element (in curves) representing achievements in business
- should look great :)

```html
<!DOCTYPE html>
<html lang="en">
<head>
<meta charset="utf-8">
<title>Business Recognition Plaque</title>
<link rel="stylesheet" href="https://fonts.googleapis.com/css2?family=Anton&family=Arimo:wght@400;700&family=Open+Sans:wght@700&family=Roboto+Condensed:wght@700&display=swap">
<style>
  :root {
    --backdrop: #e6cbb0;
    --wood-dark: #4a2a18;
    --wood-mid: #6b4029;
    --wood-light: #85553a;
    --brass-light: #f3e08a;
    --brass-mid: #dcc058;
    --brass-deep: #b8963a;
    --ink: #0d0d0d;
    --ribbon: #d6262b;
    --ribbon-dark: #b01a1f;
    --screw: #c9a13a;
  }
  * { margin: 0; padding: 0; box-sizing: border-box; }
  html, body {
    width: 1200px; height: 975px; overflow: hidden;
    background: var(--backdrop);
  }
  .canvas { position: relative; width: 1200px; height: 975px; }

  .wood-panel {
    position: absolute; left: 70px; top: 75px; width: 1060px; height: 820px;
    background: linear-gradient(135deg, var(--wood-light), var(--wood-mid) 45%, var(--wood-dark));
    box-shadow: 6px 10px 18px rgba(60, 30, 10, 0.45);
    border: 4px solid var(--wood-dark);
  }
  .brass-plate {
    position: absolute; left: 112px; top: 120px; width: 973px; height: 730px;
    background:
      repeating-linear-gradient(180deg, rgba(255,255,255,0.08) 0 2px, rgba(0,0,0,0.03) 2px 4px),
      linear-gradient(135deg, var(--brass-deep), var(--brass-light) 40%, var(--brass-mid) 70%, var(--brass-deep));
    box-shadow: inset 0 0 0 2px rgba(255,245,200,0.6), 0 2px 6px rgba(0,0,0,0.5);
  }
  .screw {
    position: absolute; width: 24px; height: 24px; border-radius: 50%;
    background: radial-gradient(circle at 35% 35%, #fff3b8, var(--screw) 55%, #6e5314);
    box-shadow: 1px 2px 3px rgba(0,0,0,0.5);
  }
  .screw.top-left { left: 138px; top: 140px; }
  .screw.top-right { left: 1048px; top: 140px; }
  .screw.bottom-left { left: 138px; top: 800px; }
  .screw.bottom-right { left: 1048px; top: 800px; }

  .logo-placeholder {
    position: absolute; left: 0; width: 1200px; top: 180px; text-align: center;
    font-family: "Open Sans", sans-serif; font-weight: 700; font-size: 37px; color: var(--ink);
  }
  .ribbon-area {
    position: absolute; left: 372px; top: 262px; width: 456px; height: 128px;
    background: linear-gradient(180deg, var(--ribbon), var(--ribbon-dark));
    border-radius: 6px;
  }
  .ribbon-word {
    position: absolute; left: 0; width: 1200px; top: 284px; text-align: center;
    font-family: "Anton", sans-serif; font-size: 60px; line-height: 84px;
    letter-spacing: 1px; color: var(--ink);
  }

  .award-title {
    position: absolute; left: 0; width: 1200px; top: 430px; text-align: center;
    font-family: "Roboto Condensed", sans-serif; font-weight: 700; font-size: 46px;
    letter-spacing: 2px; color: var(--ink);
  }
  .award-line {
    position: absolute; left: 0; width: 1200px; text-align: center;
    font-family: "Arimo", sans-serif; font-size: 24px; line-height: 28px; color: var(--ink);
  }
  .award-line strong { font-weight: 700; }
  .line-to { top: 505px; }
  .line-recipient { top: 552px; font-weight: 700; }
  .line-leadership { top: 594px; }
  .line-company { top: 646px; }
  .line-council { top: 697px; }

  .award-date {
    position: absolute; left: 208px; top: 794px;
    font-family: "Arimo", sans-serif; font-size: 24px; line-height: 28px; color: var(--ink);
  }
  .signature-block {
    position: absolute; left: 862px; top: 790px; width: 154px; text-align: center;
    border-top: 1px solid var(--ink); padding-top: 4px;
    font-family: "Arimo", sans-serif; font-size: 24px; line-height: 28px; color: var(--ink);
  }
</style>
</head>
<body>
<main class="canvas">
  <div class="wood-panel"></div>
  <div class="brass-plate"></div>
  <span class="screw top-left"></span>
  <span class="screw top-right"></span>
  <span class="screw bottom-left"></span>
  <span class="screw bottom-right"></span>

  <p class="logo-placeholder">put your logo here</p>

  <div class="ribbon-area" role="img" aria-label="Red ribbon banner ornament"></div>
  <p class="ribbon-word">RECOGNITION</p>

  <h1 class="award-title">The Best Entrepreneur in 2013</h1>
  <p class="award-line line-to">to</p>
  <p class="award-line line-recipient">Mr. Daniel R. Whitford, MBA</p>
  <p class="award-line line-leadership">Under the leadership of <strong>Mr. Daniel R. Whitford, MBA</strong></p>
  <p class="award-line line-company">the company <strong>DR-WHITFORD Ltd</strong> has been selected</p>
  <p class="award-line line-council">by a City Council as the best company of The City.</p>

  <p class="award-date">Date : 4th July, 2013</p>
  <p class="signature-block">City Mayor</p>
</main>
</body>
</html>
```